Brixtondel - eCommerce Design and Shopify Theme customisation

eCommerce Website Design - firstly with mockups then once we have chosen the design the successful designer will need to choose, purchase and customise a Shopify theme to match the design. We have a logo already designed and now want to create our web presence based on carrying up to 50 products on our website.
Target Market(s)
UK Pet Owners
Industry/Entity Type
Pet Shop
Requirements
Must have
- Design must be achievable using a customised Shopify theme - the successful designer will be responsible for the delivery of a working theme on our shopify website.
Should not have
- should not look cheap or have designs that aren't compatible or achievable with Shopify

```html
<!DOCTYPE html>
<html lang="en">
<head>
<meta charset="utf-8">
<title>Brixtondel – Pet Supplies</title>
<link href="https://fonts.googleapis.com/css2?family=Questrial&family=Barlow:wght@400;500&display=swap" rel="stylesheet">
<style>
:root{
  --gold:#d6b641;
  --gold-soft:#f1e6c5;
  --purple:#8767ad;
  --ink:#1d1d1f;
  --muted:#8a8a8a;
  --card:#f7f7f8;
  --line:#e6e6e6;
  --white:#ffffff;
}
*{box-sizing:border-box;margin:0;padding:0}
html,body{width:1200px;height:2304px;overflow:hidden;background:var(--white)}
body{position:relative;font-family:"Questrial",sans-serif;color:var(--ink)}
.abs{position:absolute}

/* header */
.brand{left:75px;top:38px;display:flex;align-items:center;gap:8px;font-size:22px;color:var(--ink)}
.brand-dot{width:22px;height:22px;border-radius:50%;background:var(--gold)}
.search{left:342px;top:30px;width:516px;height:49px;border:1px solid var(--line);border-radius:4px;display:flex;align-items:center;padding-left:16px;gap:14px;color:#9a9a9a;font-size:14px}
.head-icon{top:38px}

/* nav */
.nav{left:0;top:108px;width:1200px;height:46px;background:var(--gold);display:flex;align-items:center;padding:0 75px;font-size:16px}
.nav a{color:var(--ink);text-decoration:none;margin-right:34px;position:relative}
.nav a.active{color:var(--white)}
.nav a.active:after{content:"";position:absolute;left:0;right:0;bottom:-15px;height:2px;background:var(--white)}
.phone{margin-left:auto;display:flex;align-items:center;gap:10px;font-size:16px}

/* perks */
.perks{left:0;top:154px;width:1200px;height:92px;background:var(--purple);color:var(--white)}
.perk{position:absolute;top:26px;display:flex;gap:12px;align-items:flex-start}
.perk b{display:block;font-weight:400;font-size:17px}
.perk small{font-size:12px}
.perk-sep{position:absolute;top:28px;width:1px;height:36px;background:rgba(255,255,255,.5)}

/* hero */
.hero-bg{left:0;top:246px;width:1200px;height:416px;background:var(--gold-soft)}
.hero{left:75px;top:304px;width:1050px;height:455px;background:var(--gold);border-radius:14px;overflow:hidden}
.hero h1{position:absolute;left:65px;top:76px;width:420px;font-weight:400;font-size:39px;line-height:43px;color:var(--white);letter-spacing:-.5px}
.hero p{position:absolute;left:66px;top:228px;font-size:15px;color:var(--white)}
.btn{display:inline-flex;align-items:center;justify-content:center;background:var(--purple);color:var(--white);border-radius:23px;font-size:16px}
.hero .btn{position:absolute;top:318px;width:157px;height:45px}
.hero-photo{position:absolute;left:495px;top:106px;width:555px;height:349px;background:linear-gradient(90deg,rgba(255,255,255,.25),rgba(80,80,80,.35) 50%,rgba(255,255,255,.45));border-radius:120px 120px 0 0}
.arrow{width:48px;height:48px;border-radius:50%;background:var(--gold-soft);top:508px;display:flex;align-items:center;justify-content:center}
.dot{top:777px;width:12px;height:12px;border-radius:50%}

/* products */
.section-title{left:0;width:1200px;text-align:center}
.tab{top:983px;width:125px;height:50px;border-radius:25px;display:flex;align-items:center;justify-content:center;gap:8px;font-size:17px}
.product{top:1228px;width:250px;height:282px;background:var(--card);border-radius:12px;text-align:center}
.pack{position:absolute;left:75px;top:-113px;width:100px;height:148px;border-radius:4px}
.product h3{position:absolute;left:20px;right:20px;top:55px;font-weight:400;font-size:16px;line-height:20px}
.price{position:absolute;left:0;right:0;top:139px;color:var(--purple);font-size:17px}
.qty{position:absolute;left:83px;top:176px;display:flex;border:1px solid var(--ink);height:24px}
.qty span{width:28px;display:flex;align-items:center;justify-content:center;font-size:13px;border-right:1px solid var(--ink)}
.qty span:last-child{border-right:0}
.select{position:absolute;left:25px;top:222px;width:200px;height:24px;border:1px solid var(--line);background:var(--white);font-size:11px;text-align:left;padding:5px 8px;display:flex;justify-content:space-between}
.product .btn{position:absolute;left:50px;top:266px;width:150px;height:34px;font-size:13px}

/* beds */
.divider{left:390px;top:1612px;width:420px;height:1px;background:var(--line)}
.feature{font-family:"Barlow",sans-serif;width:200px}
.feature b{display:block;font-weight:500;font-size:19px}
.feature small{display:block;font-size:13px;color:var(--muted);line-height:15px}
.thumb{width:76px;height:76px;border-radius:50%;background:radial-gradient(circle at 55% 50%,#8a7a6a 0 30%,#cfc6bd 31% 60%,#f3e4c2 61%)}
.thumb.vet{background:radial-gradient(circle at 55% 55%,#a27c4f 0 35%,#d9d3e9 36%)}
</style>
</head>
<body>

<header>
  <div class="abs brand"><span class="brand-dot"></span>Brixtondel</div>
  <div class="abs search">
    <svg width="20" height="20" viewBox="0 0 20 20" fill="none" stroke="#1d1d1f" stroke-width="2"><circle cx="8" cy="8" r="6"/><path d="M13 13l5 5"/></svg>
    Search our store
  </div>
  <svg class="abs head-icon" style="left:1037px" width="28" height="30" viewBox="0 0 28 30" fill="none" stroke="#1d1d1f" stroke-width="2"><circle cx="14" cy="9" r="7"/><path d="M2 29c0-7 5-11 12-11s12 4 12 11z"/></svg>
  <svg class="abs head-icon" style="left:1104px" width="24" height="30" viewBox="0 0 24 30" fill="none" stroke="#1d1d1f" stroke-width="2"><rect x="2" y="9" width="20" height="20" rx="3"/><path d="M7 9V6a5 5 0 0 1 10 0v3"/></svg>
</header>

<nav class="abs nav">
  <a class="active">Home</a><a>Dog</a><a>Cat</a><a>Shop</a><a>Blogs</a><a>Contact Us</a>
  <div class="phone">
    <svg width="22" height="22" viewBox="0 0 24 24" fill="none" stroke="#1d1d1f" stroke-width="1.6"><path d="M5 3l4 1 1 5-2 2a12 12 0 0 0 5 5l2-2 5 1 1 4c-1 2-3 2-5 2C9 20 4 15 3 8c0-2 0-4 2-5z"/><path d="M14 5a5 5 0 0 1 5 5M14 1a9 9 0 0 1 9 9"/></svg>
    0123 000 4567
  </div>
</nav>

<section class="abs perks">
  <div class="perk" style="left:75px">
    <svg width="42" height="34" viewBox="0 0 42 34" fill="none" stroke="#fff" stroke-width="1.6"><path d="M2 6h24v20H2zM26 12h8l6 7v7H26"/><circle cx="9" cy="28" r="3"/><circle cx="32" cy="28" r="3"/></svg>
    <div><b>Free delivery</b><small>when you spend £35 or more*</small></div>
  </div>
  <div class="perk-sep" style="left:382px"></div>
  <div class="perk" style="left:448px">
    <svg width="38" height="36" viewBox="0 0 38 36" fill="none" stroke="#fff" stroke-width="1.6"><circle cx="20" cy="20" r="14"/><path d="M20 12v8l5 4M16 2h8M4 16h6M2 22h8"/></svg>
    <div><b>New!</b><small>One hour delivery slots</small></div>
  </div>
  <div class="perk-sep" style="left:700px"></div>
  <div class="perk" style="left:766px">
    <svg width="40" height="40" viewBox="0 0 40 40" fill="none" stroke="#fff" stroke-width="1.6"><rect x="2" y="10" width="26" height="26" rx="2"/><path d="M6 24h4M12 24h4M18 24h4M6 30h4M12 30h4"/><circle cx="28" cy="12" r="10" fill="#8767ad"/><path d="M28 6v12M22 12h12"/></svg>
    <div><b>Save 10%</b><small>on your first Repeat Delivery</small></div>
  </div>
</section>

<div class="abs hero-bg"></div>
<section class="abs hero">
  <h1>Welcome to The UK’s favourite online Pet Supplies Store!</h1>
  <p>Find their favourite brands, or try one that’s new.</p>
  <span class="btn" style="left:66px">Shop for Dogs</span>
  <span class="btn" style="left:241px">Shop for Cats</span>
  <div class="hero-photo" role="img" aria-label="Photo of two dogs and two cats sitting together"></div>
</section>
<div class="abs arrow" style="left:51px"><svg width="28" height="16" viewBox="0 0 28 16" fill="none" stroke="#d6b641" stroke-width="2"><path d="M27 8H2M9 1L2 8l7 7"/></svg></div>
<div class="abs arrow" style="left:1101px"><svg width="28" height="16" viewBox="0 0 28 16" fill="none" stroke="#d6b641" stroke-width="2"><path d="M1 8h25M19 1l7 7-7 7"/></svg></div>
<span class="abs dot" style="left:583px;background:var(--gold)"></span>
<span class="abs dot" style="left:604px;border:1px solid var(--line)"></span>

<section>
  <h2 class="abs section-title" style="top:870px;font-weight:400;font-size:38px;letter-spacing:-.5px">Our Products</h2>
  <p class="abs section-title" style="top:922px;font-size:17px;color:var(--muted)">Treat Them to the Good Stuff</p>
  <div class="abs tab" style="left:467px;background:var(--gold)">
    <svg width="34" height="30" viewBox="0 0 34 30" fill="none" stroke="#1d1d1f" stroke-width="1.6"><path d="M9 6c-5 0-8 6-6 11l5-2M25 6c5 0 8 6 6 11l-5-2"/><path d="M9 6c2-4 14-4 16 0l1 14c0 5-4 8-9 8s-9-3-9-8z"/><circle cx="13" cy="15" r="1"/><circle cx="21" cy="15" r="1"/><path d="M15 21h4"/></svg>Dog
  </div>
  <div class="abs tab" style="left:608px;border:1px solid var(--line)">
    <svg width="40" height="28" viewBox="0 0 40 28" fill="none" stroke="#1d1d1f" stroke-width="1.6"><path d="M10 4l5 6h10l5-6 1 12c0 7-5 10-11 10S9 23 9 16z"/><circle cx="16" cy="15" r="1"/><circle cx="24" cy="15" r="1"/><path d="M2 16h8M2 20h8M30 16h8M30 20h8"/></svg>Cat
  </div>

  <article class="abs product" style="left:75px">
    <div class="pack" style="background:linear-gradient(#f3b21b,#e58a14)" role="img" aria-label="Dog treat pack"></div>
    <h3>Brightbite Dental Medium Adult Dog Treat 7 Stick</h3>
    <div class="price">Only £2.40</div>
    <div class="qty"><span>+</span><span>1</span><span>−</span></div>
    <div class="select">Deliver once <span>⌄</span></div>
    <span class="btn">Add to Basket</span>
  </article>
  <article class="abs product" style="left:342px">
    <div class="pack" style="background:linear-gradient(#6f8d4a,#c6a55a)" role="img" aria-label="Dry dog food bag"></div>
    <h3>Hollowfield Turkey &amp; Rice Adult Dog Food 15kg</h3>
    <div class="price">Only £53.63</div>
    <div class="qty"><span>+</span><span>1</span><span>−</span></div>
    <div class="select">Deliver once <span>⌄</span></div>
    <span class="btn">Add to Basket</span>
  </article>
  <article class="abs product" style="left:608px">
    <div class="pack" style="background:linear-gradient(#2a3d8f,#3f8fd6)" role="img" aria-label="Dry cat food bag"></div>
    <h3>Feline First Chicken &amp; Wheat Light Adult Cat Food</h3>
    <div class="price" style="top:136px">Only £2.40</div>
    <div class="qty" style="top:173px"><span>+</span><span>1</span><span>−</span></div>
    <div class="select" style="top:219px">Deliver once <span>⌄</span></div>
    <span class="btn" style="top:265px">Add to Basket</span>
  </article>
  <article class="abs product" style="left:875px">
    <div class="pack" style="left:88px;width:74px;background:linear-gradient(#c9c9cc,#8d8d92 70%,#d24040)" role="img" aria-label="Dry cat food bag"></div>
    <h3>Vitacore Sense Original Salmon Dry Adult Cat Food 10kg</h3>
    <div class="price" style="top:137px">Only £2.40</div>
    <div class="qty" style="top:174px"><span>+</span><span>1</span><span>−</span></div>
    <div class="select" style="top:220px">Deliver once <span>⌄</span></div>
    <span class="btn">Add to Basket</span>
  </article>
</section>

<div class="abs divider"></div>

<section>
  <svg class="abs" style="left:0;top:1630px" width="1200" height="620" viewBox="0 0 1200 620" fill="none">
    <path d="M0 18c120 22 250 30 380 28S700 10 900 8s240 12 300 30" stroke="#f4c400" stroke-width="4" opacity=".8"/>
    <path d="M0 30 C200 50 500 60 1200 30 V560 C900 520 500 600 0 560Z" fill="#f6f4f8" opacity=".7"/>
    <path d="M0 556c160 30 340 40 520 22s420-40 680-2" stroke="#f4c400" stroke-width="4" opacity=".8"/>
  </svg>
  <div class="abs" style="left:425px;top:1740px;width:390px;height:370px;border-radius:40% 40% 45% 45%;background:radial-gradient(ellipse at 50% 35%,#c9823a 0 28%,#d8c08f 45%,rgba(255,255,255,0) 70%)" role="img" aria-label="Photo of a ginger kitten in a wicker basket"></div>

  <div class="abs feature" style="left:63px;top:1765px;text-align:right"><b>Beautify Cat Bads</b><small>Canis certified cat trainers<br>specialize in behavior.</small></div>
  <div class="abs thumb" style="left:283px;top:1742px" role="img" aria-label="Felt cat cave bed"></div>
  <div class="abs feature" style="left:43px;top:1921px;text-align:right"><b>Vet Bed</b><small>Canis certified cat trainers<br>specialize in behavior.</small></div>
  <div class="abs thumb vet" style="left:269px;top:1895px" role="img" aria-label="Padded pet bed"></div>
  <div class="abs feature" style="left:63px;top:2078px;text-align:right"><b>Beautify Cat Bads</b><small>Canis certified cat trainers<br>specialize in behavior.</small></div>
  <div class="abs thumb" style="left:283px;top:2061px" role="img" aria-label="Felt cat cave bed"></div>

  <div class="abs thumb" style="left:858px;top:1742px" role="img" aria-label="Felt cat cave bed"></div>
  <div class="abs feature" style="left:955px;top:1751px"><b>Beautify Cat Bads</b><small>Canis certified cat trainers<br>specialize in behavior.</small></div>
  <div class="abs thumb" style="left:880px;top:1911px" role="img" aria-label="Felt cat cave bed"></div>
  <div class="abs feature" style="left:969px;top:1921px"><b>Beautify Cat Bads</b><small>Canis certified cat trainers<br>specialize in behavior.</small></div>
  <div class="abs thumb" style="left:846px;top:2061px" role="img" aria-label="Felt cat cave bed"></div>
  <div class="abs feature" style="left:958px;top:2074px"><b>Beautify Cat Bads</b><small>Canis certified cat trainers<br>specialize in behavior.</small></div>
</section>

</body>
</html>
```